Flyer-Design
Zielgruppe
Dienstleistungen
Aufgabenstellung
Unser Folder, Din lang, 6-seitig,
soll eine neue Farbe (blau) erhalten und unser Firmenlogo muss implementiert werden.
Sonst nix. Keine weiteren Änderungen nötig/erwünscht.
Texte werden in kopierbarer Version gestellt
Der Folder wird bei Papiermondo in den Druck gegeben, deren Druckvorgaben (Beschnitt etc.) sind einzuhalten.

```html
<!DOCTYPE html>
<html lang="de">
<head>
<meta charset="utf-8">
<title>Seniovita Folder – Innenseiten</title>
<link href="https://fonts.googleapis.com/css2?family=Arimo:wght@400;700&display=swap" rel="stylesheet">
<style>
  :root {
    --blue-deep: #2a4a9c;
    --blue-sub: #3b59b0;
    --bg-left: #6a80c4;
    --bg-mid: #b4c1e6;
    --bg-right: #ffffff;
    --text: #1a1a1a;
  }
  * { box-sizing: border-box; margin: 0; padding: 0; }
  html, body { width: 1200px; height: 850px; overflow: hidden; }
  body {
    font-family: "Arimo", Arial, sans-serif;
    color: var(--text);
    font-size: 10.4px;
    line-height: 14.6px;
  }
  .spread {
    position: relative;
    width: 1200px; height: 850px;
    background: linear-gradient(90deg, var(--bg-left) 0%, #93a5d8 30%, var(--bg-mid) 52%, #e3e8f6 75%, var(--bg-right) 100%);
    overflow: hidden;
  }
  .panel { position: absolute; }
  .panel--situation { left: 54px; top: 40px; width: 300px; }
  .panel--philosophy { left: 459px; top: 40px; width: 305px; }
  .panel--concept { left: 459px; top: 505px; width: 305px; }
  .panel--terms { left: 855px; top: 0; width: 290px; height: 850px; }

  .section-title {
    font-size: 23px; line-height: 28px; font-weight: 700;
    color: var(--blue-deep);
    padding-bottom: 5px;
    border-bottom: 2px solid var(--blue-deep);
    margin-bottom: 26px;
    letter-spacing: 0.2px;
  }
  .lead { font-weight: 700; margin-bottom: 14px; }
  p { margin-bottom: 14px; }
  .slogan {
    position: absolute; left: 54px; top: 517px;
    font-weight: 700; font-size: 11.5px;
  }
  .photo {
    position: absolute; left: 52px; top: 568px;
    width: 224px; height: 224px; border-radius: 50%;
    border: 3px solid var(--blue-deep);
    background: radial-gradient(circle at 45% 40%, #e8ddd2 0%, #b9a58e 45%, #6f6656 100%);
  }
  .subhead {
    font-size: 10.6px; font-weight: 700; color: var(--blue-sub);
    margin-bottom: 10px; text-transform: uppercase; line-height: 14px;
  }
  .panel--concept p { margin-bottom: 12px; }
  .term { position: absolute; left: 0; width: 290px; }
  .term--hours { top: 106px; }
  .term--duration { top: 227px; }
  .term--german { top: 406px; }
  .term--invoice { top: 627px; }
  .term--notice { top: 718px; }
  .levels { width: 100%; border-collapse: collapse; margin-top: 6px; }
  .levels td { padding: 0 0 12px 0; vertical-align: top; line-height: 14px; }
  .levels td:first-child { width: 152px; }
</style>
</head>
<body>
<main class="spread">

  <section class="panel panel--situation">
    <h2 class="section-title">SITUATION</h2>
    <p class="lead">Sie haben einen Angehörigen, der Betreuung benötigt?</p>
    <p>Die notwendige Unterstützung überschreitet Ihre zeitlichen oder auch physischen und psychischen Möglichkeiten?</p>
    <p>Ihnen liegt viel daran, dass die Ihnen nahestehende Person die bestmögliche Betreuung erhält?</p>
    <p>Sie möchten nicht, dass Ihr Angehöriger seinen Lebensabend in einem Altenheim verbringen muss?</p>
    <p>Wir möchten und können Ihnen weiterhelfen!</p>
    <p>Wir vermitteln Ihnen liebevolle osteuropäische Betreuungskräfte (w/m) Haushaltshilfen, die sich um Rahmen der 24h Pflege um Ihren Angehörigen kümmern.</p>
    <p>Auch wenn die osteuropäische Betreuerin bei Ihnen ist, stehen wir Ihnen weiterhin mit Rat und Tat zur Verfügung.</p>
    <p>Die Betreuungskraft wohnt bei Ihrem Angehörigen und kann der immer zur Verfügung stehen, wenn sie gebraucht wird.</p>
    <p>Gern arbeiten wir auch mit örtlichen, ambulanten Pflegediensten zusammen. Die Mitarbeiter/innen des Pflegedienstes übernehmen bei dieser Konstellation die pflegerischen Maßnahmen, unsere Betreuerin kümmert sich um die Haushaltsführung und andere anfallende Aufgaben.</p>
  </section>
  <p class="slogan">SENIOVITA – BETREUUNG MIT HERZ</p>
  <div class="photo" role="img" aria-label="Foto: lächelnde Betreuerin umarmt eine ältere Dame"></div>

  <section class="panel panel--philosophy">
    <h2 class="section-title">PHILOSOPHIE</h2>
    <p class="lead">„Einen alten Baum verpflanzt man nicht“</p>
    <p>In aller Regel fühlt sich eine pflege-/hilfsbedürftige Person in ihrer angestammten Umgebung am wohlsten!</p>
    <p>Sie befinden sich zurzeit vermutlich an dem Punkt, an dem Sie prüfen, wie die Pflege und Betreuung eines nahen Angehörigen zu organisieren ist und sicherlich überlegen Sie auch, ob Ihr Angehöriger vielleicht in einem Pflegeheim gut aufgehoben sein könnte.</p>
    <p>Ein Seniorenheim ist oftmals die einfachste Lösung – für die Angehörigen. Entspricht diese Lösung aber auch dem Wunsch der betroffenen Person? Das Pflegepersonal in deutschen Senioreneinrichtungen ist aus Kostengründen meist auf das Minimum begrenzt, eine umfassende, fürsorgliche Pflege zeitlich häufig gar nicht möglich.</p>
    <p>Wir sagen nicht, dass die von uns vermittelten Betreuungskräfte grundsätzlich und immer vom Himmel gefallen sind und dass die „Rund-um-die-Uhr“ Seniorenbetreuung in den eigenen vier Wänden grundsätzlich immer vorzuziehen ist, aber die Wahrscheinlichkeit, dass es der zu betreuenden Person zu Hause, wo sich eine Betreuungskraft nur um sie kümmert, besser geht und gefällt als in einem Pflegeheim, ist doch erheblich.</p>
  </section>

  <section class="panel panel--concept">
    <h2 class="section-title">KONZEPT</h2>
    <h3 class="subhead">1. 24 Stunden Pflege</h3>
    <p>Die osteuropäische Betreuerin wohnt bei der zu betreuenden Person und kann sich so jederzeit um diese kümmern. Sie führt den Haushalt, übernimmt Hilfestellungen bei der Grundpflege, z.B. bei der Körperpflege, beim An- und Ausziehen, wechselt Windeln, falls erforderlich, führt Gespräche und begleitet die zu betreuende Person bei Arztbesuchen oder Spaziergängen.</p>
    <h3 class="subhead">2. Rahmenbedingungen</h3>
    <p>Die Betreuungskraft benötigt ein eigenes Zimmer (Grundvoraussetzung), im Winter heizbar, in dem ein Bett steht. Die Mitbenutzung eines Badezimmers muss natürlich auch möglich sein; alles Andere kann unterschiedlich/flexibel gestaltet werden. Kost und Logis sind im Rahmen des normalen Verbrauchs frei.</p>
  </section>

  <section class="panel panel--terms">
    <div class="term term--hours">
      <h3 class="subhead">3. Arbeitszeit bei der 24 Stunden Senioren-<br>pflege</h3>
      <p>Die Anwesenheit beträgt 24 Stunden. Aber natürlich benötigt die Betreuungskraft auch Freizeit, sie kann nicht 24h am Tag arbeiten.</p>
    </div>
    <div class="term term--duration">
      <h3 class="subhead">4. Einsatzdauer</h3>
      <p>Die Betreuer/innen haben ihre Heimat in Polen/Tschechien/Slowakei. Daher möchten die meisten Betreuungskräfte nach etwa 8 bis 12 Wochen, für eine begrenzte Zeit nach Hause. In diesem Fall oder auch bei einem gewünschten Wechsel Ihrerseits, sorgt Seniovita umgehend für einen gleichwertigen Ersatz. Häufig wechseln sich zwei oder drei Betreuungskräfte gegenseitig ab. Der Übergang bei einem Wechsel ist nahtlos.</p>
    </div>
    <div class="term term--german">
      <h3 class="subhead">5. Deutschkenntnisse</h3>
      <p>Hier bieten wir 5 Abstufungen an:</p>
      <table class="levels">
        <tr><td>Geringe Kenntnisse:</td><td>Verstehen / Sprechen wenig</td></tr>
        <tr><td>Ausreichende Kenntnisse:</td><td>Einfache Gespräche</td></tr>
        <tr><td>Mittlere Kenntnisse:</td><td>Vieles wird verstanden</td></tr>
        <tr><td>Gute Kenntnisse:</td><td>Detaillierte Gespräche</td></tr>
        <tr><td>Sehr gute Kenntnisse:</td><td>Ohne Einschränkungen</td></tr>
      </table>
    </div>
    <div class="term term--invoice">
      <h3 class="subhead">6. Rechnungen</h3>
      <p>Jeweils zum Monatsende erhalten Sie eine Rechnung. Der Rechnungsausgleich erfolgt per Überweisung.</p>
    </div>
    <div class="term term--notice">
      <h3 class="subhead">7. Kündigungsfristen</h3>
      <p>Die Verträge können, ohne Angabe von Gründen, mit einer Frist von 7 Tagen gekündigt werden.</p>
    </div>
  </section>

</main>
</body>
</html>
```